Dynamic Lead Design (Partial WebPage)

To encourage visitors to our website to donate to our organization, we would like to replace the Dynamic Lead on our website with one that will evoke emotion from the viewer and motivate them to donate generously.

The deliverable should be a mockup of the design in context of the current website. See attached file for editable area. Fonts used in the mockup should be code-able in HTML/CSS.

The website
http://www.hopelark.org

Please use this wireframe for reference:
http://app.mockvane.com/8b1c47e20f93d5a6c71e04b28d9a3f5e17c6b0d2/7315824

Content:
[Image should evoke emotion from the viewer and motivate them to donate generously.]
Headline - “Give to TIDEL.”
Sub Headline - “Cancer patients find answers here. Your donation makes that possible.”
Call to action label - “Donate”

We love these examples:

Bright Oak Harvest Drive (http://www.hd.brightoak.org/brightoak/v/index.jsp?vgnextoid=7a5d3f81c2e9b460VgnVCM100000318274bdRCRD)
Well Meadow (http://www.wellmeadow.org/)

Design Size:
width: 971px
height: 300px

***see attached document for design area***

- Organization Background -

Our website receives over 40,000 unique visitors each month - mostly cancer patients and their family members seeking information about their disease. We would like to drive our visitors to donate to our nonprofit throughout late November and December (the majority of our donations from individuals come in during that time period).

We will be mailing an appeal letter to our database in mid-November. With this banner ad, we seek to complement that appeal. Some key messages from our appeal are:

- We focus on getting patients and their loved ones the best, most up-to-date information from trusted doctors who are leaders in cancer research – for free. We don’t sell a particular product or procedure. We simply arm them with the most current information so they can make the best decision for their own (or their loved one’s) care.

- What is the value of the support they or someone they know has received from our organization? Twenty-five dollars? One hundred dollars? One thousand? Can you even put an amount to it? Whatever it is, please consider making an end of year donation to this organization that has helped so many, comforted hundreds of thousands of patients and caretakers, and been there when needed.

- 2014 will be a year of growth. We just hired our first executive director. She is experienced in helping small nonprofits grow in size, revenue, and scope, and will undoubtedly bring a new level of energy to our work.

- In just a few months, we will hold two patient forums – first-of-its-kind programs for the organization. As we continue to grow, we will be able to offer more of these types of programs to more patients throughout the US.

Industry/Entity Type

Charity

Requirements
Must have
• - Must Adhere to existing website branding

```html
<!DOCTYPE html>
<html lang="en">
<head>
<meta charset="utf-8">
<title>TIDEL – Give to TIDEL</title>
<link rel="stylesheet" href="https://fonts.googleapis.com/css2?family=Arimo:wght@400;700&family=Open+Sans:wght@400;600;700&display=swap">
<style>
:root{
  --mint:#6ccca6;
  --mint-soft:#d6efe3;
  --salmon:#f59c85;
  --taupe:#a38a82;
  --slate:#808080;
  --ink:#333333;
  --link:#1e8c4e;
  --rule:#dddddd;
  --white:#ffffff;
}
*{box-sizing:border-box;margin:0;padding:0}
html,body{width:1047px;height:1200px;overflow:hidden;background:var(--white)}
body{position:relative;font-family:"Arimo",Arial,sans-serif;color:var(--ink)}
.abs{position:absolute}

/* header */
.brand{left:45px;top:38px;width:175px;display:flex;align-items:center;gap:10px}
.brand-dot{flex:none;width:74px;height:74px;border-radius:50%;background:var(--salmon)}
.brand-name{font-family:"Open Sans",sans-serif;font-weight:700;font-size:26px;color:var(--mint);letter-spacing:1px;white-space:nowrap}
.brand-tag{left:230px;top:40px;width:105px;font-family:"Open Sans",sans-serif;font-weight:700;font-size:13px;line-height:16px;color:var(--taupe)}
.search{left:476px;top:45px;width:403px;height:58px;border:5px solid var(--mint-soft);border-radius:22px;background:var(--white)}
.search-field{position:absolute;left:24px;top:12px;width:285px;height:24px;border:1px solid #bbb;font-size:10px;color:#999;padding:5px 6px}
.search-btn{position:absolute;left:314px;top:12px;width:54px;height:24px;background:var(--mint-soft);border:1px solid #b6dcc8;font-size:11px;font-weight:700;text-align:center;line-height:22px}
.search-x{position:absolute;left:376px;top:13px;font-size:13px;color:#888}

/* nav */
.nav{left:45px;top:152px;display:flex;gap:3px}
.nav a{display:flex;align-items:center;justify-content:center;height:45px;color:var(--white);text-decoration:none;font-family:"Open Sans",sans-serif;font-weight:600;font-size:14px;letter-spacing:1.2px;line-height:15px;text-align:center;background:var(--mint);white-space:nowrap}
.nav .profile{background:var(--slate)}
.nav .donate{background:var(--salmon)}
.donate-bump{left:957px;top:115px;width:58px;height:58px;border-radius:50%;background:var(--salmon)}

/* lead */
.lead-panel{top:206px;height:285px;font-family:"Open Sans",sans-serif;font-size:19px;line-height:23px;color:var(--white)}
.lead-panel span{position:absolute;display:block}
.lead-sad{left:45px;width:241px;background:var(--taupe);border-radius:3px 0 0 3px}
.lead-sad span{left:67px;top:58px;width:165px}
.lead-hope{left:287px;width:241px;background:var(--mint);border-radius:0 3px 3px 0}
.lead-hope span{left:20px;top:61px;width:125px}
.lead-title{left:541px;top:302px;font-family:"Open Sans",sans-serif;font-weight:600;font-size:33px;color:#3a3a3a;letter-spacing:-.5px}
.lead-sub{left:541px;top:348px;font-family:"Open Sans",sans-serif;font-size:14.5px;color:#3a3a3a;letter-spacing:-.2px;white-space:nowrap}
.lead-cta{left:541px;top:414px;width:465px;height:52px;background:var(--salmon);border-radius:3px;color:var(--white);font-family:"Open Sans",sans-serif;font-size:27px;text-align:center;line-height:52px}

/* main column */
.edit{left:57px;top:516px;font-size:13px;font-weight:700;color:#555}
.section-title{left:45px;top:577px;font-size:18px;font-weight:700;color:#666}
.share{left:519px;top:565px;width:198px;height:18px;border:1px solid #e05a5a;border-radius:2px;display:flex;align-items:center;gap:2px;padding-left:3px;font-size:12px}
.share i{display:block;width:12px;height:12px;background:#7a8fb5}
.share span{margin-left:3px}
.post{left:45px;width:688px}
.post h2{font-size:17px;line-height:21px;font-weight:700;color:var(--link)}
.post .meta{font-size:13.5px;margin-top:2px;color:#333;word-spacing:4px}
.post .meta b{font-weight:700}
.post .meta em{font-style:normal;font-weight:700;color:var(--link);word-spacing:1px}
.post p{font-size:15.6px;line-height:20px;margin-top:16px}
.post p a{font-style:italic;color:var(--link);text-decoration:none;font-size:14px}
.rule{left:45px;width:688px;height:1px;background:var(--rule)}

/* sidebar */
.social{left:783px;top:520px;display:flex;gap:22px}
.social i{display:block;width:31px;height:31px;border-radius:4px}
.ask{left:758px;top:573px;width:243px;height:45px;background:var(--salmon);border-radius:3px;display:flex;align-items:center;padding-left:8px;gap:6px;color:var(--white);font-family:"Open Sans",sans-serif;font-size:20px;letter-spacing:1px}
.ask b{width:30px;height:30px;border-radius:50%;background:#6d6d6d;font-size:13px;display:flex;align-items:center;justify-content:center;font-weight:700}
.ask span{margin-left:14px}
.side-title{left:758px;top:645px;font-size:17px;font-weight:700;color:#666}
.side-link{left:758px;font-size:13px;font-weight:700;color:var(--link);white-space:nowrap}
.forum-box{left:758px;top:757px;width:243px;height:45px;background:var(--salmon);border-radius:3px;color:var(--white);font-family:"Open Sans",sans-serif;font-size:17px;line-height:20px;letter-spacing:1.5px;text-align:center;padding-top:2px}
.faculty{left:758px;top:909px;width:243px;height:137px;background:linear-gradient(135deg,#b49486,#d6c1b2 50%,#8a7a72)}
.faculty-note{position:absolute;left:38px;top:34px;width:170px;height:70px;background:rgba(214,239,227,.92);font-family:"Courier New",monospace;font-weight:700;font-size:12.5px;line-height:15px;color:var(--salmon);text-align:center;padding-top:4px}
.faculty-note em{display:block;color:#555;font-size:11.5px;white-space:nowrap}
.topics{left:758px;top:1074px;width:243px;display:flex;flex-direction:column;gap:2px}
.topics a{display:block;height:22px;background:var(--taupe);color:var(--white);text-decoration:none;text-align:center;font-family:"Open Sans",sans-serif;font-size:14.5px;line-height:22px;border-radius:2px}
</style>
</head>
<body>

<header>
  <div class="abs brand"><span class="brand-dot"></span><span class="brand-name">TIDEL</span></div>
  <div class="abs brand-tag">Trusted Information for Disease Education &amp; Learning</div>
  <div class="abs search">
    <div class="search-field">Site Search</div>
    <div class="search-btn">Search</div>
    <div class="search-x">✕</div>
  </div>
  <span class="abs donate-bump"></span>
  <svg class="abs" style="left:975px;top:133px" width="20" height="20" viewBox="0 0 20 20"><circle cx="10" cy="10" r="9" fill="#ffffff"/><path d="M10 5v10M5 10h10" stroke="#3fb36b" stroke-width="3"/></svg>
  <nav class="abs nav">
    <a style="width:167px">ABOUT TIDEL</a>
    <a style="width:170px">ASK US<br>DISCUSSION FORUMS</a>
    <a style="width:170px">GENERAL<br>CANCER INFO</a>
    <a style="width:170px">FOCUSED<br>CANCER INFO</a>
    <a class="profile" style="width:139px">PROFILE</a>
    <a class="donate" style="width:139px">DONATE</a>
  </nav>
</header>

<section class="lead">
  <div class="abs lead-panel lead-sad" role="img" aria-label="Illustration of a figure slumped on a raft in rough water"><span>After a diagnosis of cancer, it’s difficult to move forward.</span></div>
  <div class="abs lead-panel lead-hope" role="img" aria-label="Illustration of a figure sitting up on a raft under a rising sun"><span>TIDEL helps guide you in the right direction.</span></div>
  <h1 class="abs lead-title">Give to TIDEL.</h1>
  <p class="abs lead-sub">Cancer patients find answers here. Your donation makes that possible.</p>
  <a class="abs lead-cta">Donate</a>
</section>

<main>
  <div class="abs edit">Edit</div>
  <h2 class="abs section-title">Recent TIDEL News &amp; Posts</h2>
  <div class="abs share"><i></i><i></i><i style="background:#444"></i><i style="background:#555"></i><span>Share/Email/More</span></div>

  <article class="abs post" style="top:645px">
    <h2>Cancer Care In Crisis? The Council on Health Practice's Report: Delivering High-Quality Cancer Care: Charting a New Course For a System in Crisis; Part I: The Current Landscape</h2>
    <div class="meta">by <b>Dr. Arlen</b> on Nov 10, 2013 in <em>TIDEL :: Cancer Basics</em></div>
    <p>&nbsp;A few months ago, the Council on Health Practice released the prepublication proofs of a massive report on the state of oncology care, saying that it was in crisis in the United States. I learned about it from an email that focused on the crisis part of the title. I was bo... <a>(Read More)</a></p>
  </article>
  <div class="abs rule" style="top:833px"></div>

  <article class="abs post" style="top:863px">
    <h2>Is there a place for live educational meetings in our new online world? Would you want to come?</h2>
    <div class="meta">by <b>Dr Halvorsen</b> on Nov 8, 2013 in <em>TIDEL :: Lung Cancer</em></div>
    <p>Back in 2009, TIDEL did a live educational meeting in Seattle, geared toward patients and caregivers, that coincided with a lung cancer conference offered to physicians. It included brief (~15 minute) talks by about 10 different specialists, ranging in topics from initi... <a>(Read More)</a></p>
  </article>
  <div class="abs rule" style="top:1030px"></div>

  <article class="abs post" style="top:1060px">
    <h2>Tweet Chat Thursday: The Tissue is the Issue, Key Challenges in Biopsies and Tissue Collection</h2>
    <div class="meta">by <b>Dr Halvorsen</b> on Nov 5, 2013 in <em>TIDEL :: Lung Cancer</em></div>
    <p>This Thursday, November 7th at 8 PM Eastern, 5 PM Pacific, we'll gather in the social stream for another one hour #LCSN (lung cancer social media) tweet chat. This time, the topic will be on biopsies and tissue collection.&nbsp; Now that we've entered a new era where more an... <a>(Read More)</a></p>
  </article>
</main>

<aside>
  <div class="abs social" aria-label="Social links">
    <i style="background:#3b5a9a"></i><i style="background:#4fb7e3"></i><i style="background:#c8302a"></i><i style="background:#f08a24"></i>
  </div>
  <div class="abs ask"><b>Q:</b><b>A:</b><span>Ask Us</span></div>
  <h3 class="abs side-title">Welcome To TIDEL!</h3>
  <a class="abs side-link" style="top:674px">How To Use TIDEL</a>
  <a class="abs side-link" style="top:695px">General Cancer FAQs</a>
  <a class="abs side-link" style="top:722px">Recent TIDEL Site Post Comments</a>
  <div class="abs forum-box">TIDEL<br>Discussion Forums</div>
  <a class="abs side-link" style="top:814px">TIDEL Discussion Forum Guidelines</a>
  <a class="abs side-link" style="top:841px">Recent TIDEL Forum Activity</a>
  <a class="abs side-link" style="top:868px">Original TIDEL Archived Forums</a>
  <div class="abs faculty" role="img" aria-label="Grid of faculty member portrait photos">
    <div class="faculty-note">TIDEL is eager to bring in more great faculty members... <em>Interested? Click Here!</em></div>
  </div>
  <nav class="abs topics">
    <a>Lung/Thoracic Cancer Info</a>
    <a>Breast Cancer Info</a>
    <a>Pancreatic Cancer Info</a>
    <a>Kidney Cancer Info</a>
    <a>Bladder Cancer Info</a>
    <a>Head/Neck Cancer Info</a>
  </nav>
</aside>

</body>
</html>
```